Creative Alcoholic Beverage Package Design Needed!

We need a packaging design for a new alcoholic beverage, including the brand name. Flavours will include Sangria and Margarita, and future line extensions as well. Package will be a box (see attached dieline and example of a competitive product) in a 3 liter format. The dimensions of the box need to match the dieline, but we can be creative on the printing of the box. The product inside will be of high-quality, so the design needs to match this
Updates

Need extra days to review

Target Market(s)

25 to 40 year old, 70% female, 30% male

Colors

Designer to choose colors to be used in the design.

Requirements
Must have
• Be attractive, colourful, modern
• clearly mention the flavour, and show the components of the flavour (Sangria : red wine and citrus) - Margarita (mexican inspiration, lime, etc.)
• Have a clear "brand name" along with the flavours
• Mention the quantity (3 liters), alcohol level : 10% alc./vol.

```html
<!DOCTYPE html>
<html lang="en">
<head>
<meta charset="utf-8">
<title>Margarita Mexican Lime – 3 Liter Carton Dieline</title>
<link href="https://fonts.googleapis.com/css2?family=Big+Shoulders+Display:wght@500&family=Montserrat:wght@400;500;600&family=Raleway:wght@400&display=swap" rel="stylesheet">
<style>
  :root {
    --bg-light: #a29f9f;
    --bg-dark: #858181;
    --board: #ffffff;
    --cut-line: #d9d9d9;
    --ink: #434343;
    --title-ink: #2f2f2f;
    --lime-light: #d8ec6a;
    --lime-mid: #a9d72b;
    --lime-deep: #6fb21a;
    --glass: #e9efe6;
  }
  html, body { margin: 0; padding: 0; overflow: hidden; }
  body {
    width: 1200px; height: 1200px;
    background: radial-gradient(circle at 50% 30%, var(--bg-light), var(--bg-dark) 80%);
  }
  .canvas { display: block; width: 1200px; height: 1200px; }
  .sheet-title {
    font-family: "Raleway", sans-serif; font-size: 26px; fill: var(--title-ink); letter-spacing: 0.3px;
  }
  .panel { fill: var(--board); stroke: var(--cut-line); stroke-width: 1.5; }
  .handle-hole { fill: var(--bg-dark); stroke: var(--cut-line); stroke-width: 1.5; }
  .fold-line { stroke: var(--cut-line); stroke-width: 1.5; fill: none; }
  .tuck-guide { stroke: #cfcfcf; stroke-width: 1.2; stroke-dasharray: 4 4; fill: none; }
  .flavour-name {
    font-family: "Big Shoulders Display", sans-serif; font-weight: 500; fill: var(--ink);
  }
  .descriptor {
    font-family: "Montserrat", sans-serif; font-weight: 600; fill: var(--ink); letter-spacing: 5px;
  }
  .descriptor-rule { stroke: var(--ink); stroke-width: 1.5; }
  .alcohol-note { font-family: "Montserrat", sans-serif; font-weight: 600; font-size: 10px; fill: var(--ink); }
  .volume-box { fill: none; stroke: var(--ink); stroke-width: 1.5; }
  .volume-number { font-family: "Montserrat", sans-serif; font-weight: 400; font-size: 30px; fill: var(--ink); }
  .volume-unit { font-family: "Montserrat", sans-serif; font-weight: 600; font-size: 8px; fill: var(--ink); }
</style>
</head>
<body>
<svg class="canvas" viewBox="0 0 1500 1500" xmlns="http://www.w3.org/2000/svg">
  <defs>
    <linearGradient id="cocktail-tones" x1="0" y1="0" x2="1" y2="1">
      <stop offset="0" stop-color="#ffffff"/>
      <stop offset="0.35" stop-color="var(--lime-light)"/>
      <stop offset="0.7" stop-color="var(--lime-mid)"/>
      <stop offset="1" stop-color="var(--glass)"/>
    </linearGradient>
    <linearGradient id="lime-tones" x1="0" y1="1" x2="1" y2="0">
      <stop offset="0" stop-color="var(--lime-mid)"/>
      <stop offset="1" stop-color="var(--lime-deep)"/>
    </linearGradient>
  </defs>

  <text class="sheet-title" x="68" y="122">CREATIVE ALCOHOLIC BEVERAGE PACKAGE DESIGN</text>

  <!-- glue flap -->
  <path class="panel" d="M62 488 L122 470 L122 1250 Q122 1260 112 1260 L72 1260 Q62 1260 62 1250 Z"/>
  <line class="fold-line" x1="62" y1="1068" x2="122" y2="1068"/>
  <line class="fold-line" x1="62" y1="1094" x2="122" y2="1094"/>

  <!-- side panel left -->
  <g class="side-panel">
    <path class="panel" d="M128 465 L128 352 Q128 328 152 328 L178 328 Q188 328 188 340 Q188 385 230 385 Q272 385 272 340 Q272 328 284 328 L310 328 Q334 328 334 352 L334 465 Z"/>
    <rect class="panel" x="128" y="465" width="212" height="617"/>
    <path class="panel" d="M130 1082 L332 1082 L332 1236 Q332 1260 308 1260 L154 1260 Q130 1260 130 1236 Z"/>
    <rect role="img" aria-label="Margarita glass rim with lime wheel" x="118" y="935" width="212" height="147" fill="url(#cocktail-tones)"/>
    <circle role="img" aria-label="Lime slice" cx="276" cy="984" r="50" fill="url(#lime-tones)"/>
    <g transform="translate(245 773) rotate(90)">
      <text class="flavour-name" x="0" y="0" text-anchor="middle" dominant-baseline="middle" font-size="100" textLength="210" lengthAdjust="spacingAndGlyphs">MARGARITA</text>
    </g>
    <g transform="translate(182 767) rotate(90)">
      <line class="descriptor-rule" x1="-86" y1="0" x2="-56" y2="0"/>
      <text class="descriptor" x="0" y="3" text-anchor="middle" font-size="7" letter-spacing="3">MEXICAN LIME</text>
      <line class="descriptor-rule" x1="56" y1="0" x2="86" y2="0"/>
    </g>
  </g>

  <!-- front panel -->
  <g class="front-panel">
    <path class="panel" d="M346 465 L346 280 Q346 256 370 256 L746 256 Q770 256 770 280 L770 465 Z"/>
    <rect class="handle-hole" x="467" y="328" width="183" height="58" rx="29"/>
    <rect class="panel" x="340" y="465" width="437" height="617"/>
    <path class="panel" d="M346 1082 L770 1082 L770 1268 Q770 1292 746 1292 L370 1292 Q346 1292 346 1268 Z"/>
    <rect role="img" aria-label="Margarita cocktail glass with lime wheel and splash" x="480" y="466" width="296" height="615" fill="url(#cocktail-tones)"/>
    <circle role="img" aria-label="Lime wheel on glass rim" cx="568" cy="552" r="82" fill="url(#lime-tones)"/>
    <text class="alcohol-note" x="378" y="506">ALCOHOL LEVEL : 10% ALC./VOL.</text>
    <text class="flavour-name" x="400" y="885" font-size="190" textLength="325" lengthAdjust="spacingAndGlyphs">MARGARITA</text>
    <line class="descriptor-rule" x1="418" y1="912" x2="462" y2="912"/>
    <text class="descriptor" x="554" y="917" text-anchor="middle" font-size="11">MEXICAN LIME</text>
    <line class="descriptor-rule" x1="642" y1="912" x2="686" y2="912"/>
    <rect class="volume-box" x="379" y="989" width="38" height="60"/>
    <text class="volume-number" x="398" y="1025" text-anchor="middle">3</text>
    <text class="volume-unit" x="398" y="1040" text-anchor="middle">LITERS</text>
  </g>

  <!-- side panel right -->
  <g class="side-panel">
    <path class="panel" d="M785 465 L785 352 Q785 328 809 328 L835 328 Q845 328 845 340 Q845 385 887 385 Q929 385 929 340 Q929 328 941 328 L962 328 Q986 328 986 352 L986 465 Z"/>
    <rect class="panel" x="777" y="465" width="217" height="617"/>
    <path class="panel" d="M786 1082 L986 1082 L986 1236 Q986 1260 962 1260 L810 1260 Q786 1260 786 1236 Z"/>
    <rect role="img" aria-label="Margarita glass with lime wheel" x="795" y="466" width="198" height="144" fill="url(#cocktail-tones)"/>
    <circle role="img" aria-label="Lime slice" cx="842" cy="560" r="50" fill="url(#lime-tones)"/>
    <path class="tuck-guide" d="M825 855 L946 855 L946 935 L925 953 Q925 1030 887 1030 Q848 1030 848 953 L825 935 Z"/>
    <g transform="translate(893 773) rotate(90)">
      <text class="flavour-name" x="0" y="0" text-anchor="middle" dominant-baseline="middle" font-size="100" textLength="210" lengthAdjust="spacingAndGlyphs">MARGARITA</text>
    </g>
    <g transform="translate(831 767) rotate(90)">
      <line class="descriptor-rule" x1="-86" y1="0" x2="-56" y2="0"/>
      <text class="descriptor" x="0" y="3" text-anchor="middle" font-size="7" letter-spacing="3">MEXICAN LIME</text>
      <line class="descriptor-rule" x1="56" y1="0" x2="86" y2="0"/>
    </g>
  </g>

  <!-- back panel -->
  <g class="back-panel">
    <path class="panel" d="M1000 465 L1000 280 Q1000 256 1024 256 L1400 256 Q1424 256 1424 280 L1424 465 Z"/>
    <rect class="handle-hole" x="1112" y="320" width="200" height="68" rx="30"/>
    <rect class="panel" x="994" y="465" width="433" height="617"/>
    <path class="panel" d="M1000 1082 L1424 1082 L1424 1268 Q1424 1292 1400 1292 L1024 1292 Q1000 1292 1000 1268 Z"/>
    <rect role="img" aria-label="Margarita cocktail glass with lime wheel and splash" x="1134" y="466" width="293" height="615" fill="url(#cocktail-tones)"/>
    <circle role="img" aria-label="Lime wheel on glass rim" cx="1222" cy="552" r="82" fill="url(#lime-tones)"/>
    <text class="alcohol-note" x="1031" y="506">ALCOHOL LEVEL : 10% ALC./VOL.</text>
    <text class="flavour-name" x="1052" y="885" font-size="190" textLength="325" lengthAdjust="spacingAndGlyphs">MARGARITA</text>
    <line class="descriptor-rule" x1="1070" y1="913" x2="1114" y2="913"/>
    <text class="descriptor" x="1207" y="918" text-anchor="middle" font-size="11">MEXICAN LIME</text>
    <line class="descriptor-rule" x1="1296" y1="913" x2="1340" y2="913"/>
    <rect class="volume-box" x="1032" y="989" width="38" height="60"/>
    <text class="volume-number" x="1051" y="1025" text-anchor="middle">3</text>
    <text class="volume-unit" x="1051" y="1040" text-anchor="middle">LITERS</text>
  </g>
</svg>
</body>
</html>
```